Brightwell Cargo Brokers Limited

The Company deals with:
shipping
logistic
imports
Export
customs clearance (customs broker services); and
customers can shop online and we take care of the shipment from the United States of America to Jamaica.
(we offer freight forwarding services from USA to Kingston Jamaica
Our tagline is : Creating Waves in the Logistic Industry.
Address: Shop 6 Brindley Commercial Complex, 207-209 Pellman Road Kingston 8, Jamaica West Indies Telephone: (876)555-0192
Example of what we required can be seem: www.swiftparcelhubexample.com

```html
<!DOCTYPE html>
<html lang="en">
<head>
<meta charset="utf-8">
<title>Brightwell Cargo Brokers Limited</title>
<link href="https://fonts.googleapis.com/css2?family=Poppins:wght@300;400;500;600;700&display=swap" rel="stylesheet">
<style>
:root{
  --navy:#0b2c5a;
  --navy-deep:#0a2b58;
  --gold:#f0a80f;
  --text:#1c2b44;
  --grey-band:#efefef;
  --white:#ffffff;
}
*{margin:0;padding:0;box-sizing:border-box}
html,body{width:1200px;height:3010px;overflow:hidden}
body{font-family:"Poppins",sans-serif;color:var(--text);background:var(--white);position:relative}
.btn{position:absolute;background:var(--gold);color:var(--navy);font-weight:700;font-size:11px;letter-spacing:.3px;border-radius:20px;display:flex;align-items:center;justify-content:center;text-transform:uppercase}
.brand{position:absolute;display:flex;align-items:center;gap:8px;font-weight:600;font-size:17px;color:var(--navy);white-space:nowrap}
.brand .dot{width:26px;height:26px;border-radius:50%;background:var(--gold);flex:none}
.site-header{position:absolute;left:0;top:0;width:1200px;height:112px;background:var(--white)}
.nav a{position:absolute;top:48px;font-size:11px;color:var(--text);text-decoration:none}
.nav a.active{color:var(--gold)}
.hero{position:absolute;left:0;top:112px;width:1200px;height:600px;background:linear-gradient(90deg,#e9e2d6 0%,#e2d6c2 45%,#b99b74 75%,#8c6a45 100%)}
.hero h1{position:absolute;left:158px;top:205px;font-weight:400;font-size:55px;line-height:62px;color:var(--navy)}
.section-title{position:absolute;left:0;width:1200px;text-align:center;font-weight:400;font-size:31px;color:var(--navy);letter-spacing:.5px}
.service{position:absolute;width:240px;text-align:center}
.service .circle{width:150px;height:150px;border-radius:50%;background:var(--navy);margin:0 auto;display:flex;align-items:center;justify-content:center}
.service h3{margin-top:34px;font-size:15px;font-weight:600;color:var(--navy)}
.service p{margin-top:10px;font-size:12.5px;line-height:14px;color:var(--text)}
.ship-band{position:absolute;left:0;top:1625px;width:1200px;height:300px;background:linear-gradient(180deg,#173c6c,#12335f);color:var(--white);text-align:center}
.ship-band h2{position:absolute;left:0;top:66px;width:1200px;font-weight:400;font-size:32px;line-height:36px}
.ship-band p{position:absolute;left:0;top:152px;width:1200px;font-weight:600;font-size:12.5px}
.step{position:absolute;width:180px;text-align:center}
.step h4{font-size:15px;font-weight:600;color:var(--navy);margin-top:36px}
.shops{position:absolute;left:3px;top:2339px;width:1197px;height:256px;background:var(--grey-band)}
.shop{position:absolute;top:2488px;font-weight:600;font-size:20px;color:#2a2a2a;width:130px;text-align:center}
.site-footer{position:absolute;left:0;top:2595px;width:1200px;height:415px;background:var(--navy-deep);color:var(--white)}
.site-footer h5{position:absolute;font-size:12px;font-weight:600}
.site-footer .small{position:absolute;font-size:11px;line-height:15px}
.rule{position:absolute;left:158px;width:212px;height:1px;background:rgba(255,255,255,.2)}
.links a{position:absolute;left:522px;font-size:11px;color:var(--white);text-decoration:none}
.newsletter{position:absolute;left:742px;top:2722px;width:300px;height:37px;border-radius:20px;background:var(--white)}
.newsletter span{position:absolute;left:16px;top:11px;font-size:10.5px;color:#6b7280}
.newsletter .submit{position:absolute;right:0;top:0;width:75px;height:37px;border-radius:20px;background:var(--gold);color:var(--navy);font-weight:700;font-size:11px;display:flex;align-items:center;justify-content:center}
.arrow{position:absolute}
</style>
</head>
<body>

<header class="site-header">
  <div class="brand" style="left:158px;top:42px"><span class="dot"></span>Brightwell Cargo</div>
  <nav class="nav">
    <a class="active" style="left:471px">Home</a>
    <a style="left:549px">Services</a>
    <a style="left:641px">About</a>
    <a style="left:720px">Contact</a>
    <a style="left:811px">FAQs</a>
    <a style="left:885px">Login</a>
  </nav>
  <div class="btn" style="left:953px;top:41px;width:90px;height:30px;text-transform:none;font-size:11px">Sign Up</div>
</header>

<section class="hero" role="img" aria-label="Photo of a woman in a denim shirt checking a clipboard beside cardboard parcels in a warehouse">
  <h1>Creating Waves in the<br>Logistic Industry</h1>
  <div class="btn" style="left:160px;top:355px;width:225px;height:37px">Sign up now</div>
</section>

<h2 class="section-title" style="top:780px">What We Do</h2>

<div class="service" style="left:141px;top:862px">
  <div class="circle"><svg width="60" height="50" viewBox="0 0 60 50" fill="none" stroke="#fff" stroke-width="2.5"><rect x="4" y="6" width="14" height="12"/><rect x="4" y="20" width="14" height="12"/><rect x="4" y="34" width="14" height="12"/><rect x="22" y="14" width="18" height="26"/><path d="M40 24h10l6 8v8H40"/><circle cx="48" cy="44" r="4"/></svg></div>
  <h3>Shipping</h3>
  <p>Lorem ipsum dolor sit amet,<br>consectetur adipiscing elit, sed<br>do eiusmod tempor incididunt ut</p>
</div>
<div class="service" style="left:481px;top:862px">
  <div class="circle"><svg width="56" height="56" viewBox="0 0 56 56" fill="none" stroke="#fff" stroke-width="2.5"><rect x="18" y="6" width="24" height="28"/><path d="M23 14h14M23 20h14M23 26h8M34 32l12-12"/><rect x="6" y="34" width="14" height="14"/><rect x="22" y="34" width="14" height="14"/></svg></div>
  <h3>Logistics</h3>
  <p>Lorem ipsum dolor sit amet,<br>consectetur adipiscing elit, sed<br>do eiusmod tempor incididunt ut</p>
</div>
<div class="service" style="left:817px;top:862px">
  <div class="circle"><svg width="56" height="56" viewBox="0 0 56 56" fill="none" stroke="#fff" stroke-width="2.5"><path d="M10 6v40M4 40l6 6 6-6M26 6v14M21 15l5 5 5-5M44 6v14M39 15l5 5 5-5"/><rect x="20" y="24" width="14" height="12"/><rect x="36" y="24" width="14" height="12"/><rect x="20" y="38" width="14" height="10"/><rect x="36" y="38" width="14" height="10"/></svg></div>
  <h3>Import</h3>
  <p>Lorem ipsum dolor sit amet,<br>consectetur adipiscing elit, sed<br>do eiusmod tempor incididunt ut</p>
</div>

<div class="service" style="left:144px;top:1180px">
  <div class="circle"><svg width="56" height="56" viewBox="0 0 56 56" fill="none" stroke="#fff" stroke-width="2.5"><path d="M12 22V6M7 11l5-5 5 5M30 22V6M25 11l5-5 5 5M48 46V6M43 11l5-5 5 5"/><rect x="6" y="24" width="14" height="11"/><rect x="22" y="24" width="14" height="11"/><rect x="6" y="37" width="14" height="10"/><rect x="22" y="37" width="14" height="10"/><path d="M4 50h48"/></svg></div>
  <h3>Export</h3>
  <p>Lorem ipsum dolor sit amet,<br>consectetur adipiscing elit, sed<br>do eiusmod tempor incididunt ut</p>
</div>
<div class="service" style="left:484px;top:1180px">
  <div class="circle"><svg width="56" height="56" viewBox="0 0 56 56" fill="none" stroke="#fff" stroke-width="2.5"><rect x="6" y="6" width="24" height="40"/><path d="M11 14h14M11 21h14M11 28h10"/><path d="M42 6v16M37 17l5 5 5-5"/><rect x="26" y="30" width="22" height="18"/></svg></div>
  <h3>Custom Clearance</h3>
  <p>Lorem ipsum dolor sit amet,<br>consectetur adipiscing elit, sed<br>do eiusmod tempor incididunt ut</p>
</div>
<div class="service" style="left:816px;top:1180px">
  <div class="circle"><svg width="56" height="56" viewBox="0 0 56 56" fill="none" stroke="#fff" stroke-width="2.5"><path d="M22 4h12M20 10h16v8H20z"/><rect x="14" y="20" width="28" height="16"/><path d="M21 20v16M28 20v16M35 20v16M6 38h44l-6 10H12z M4 52h48"/></svg></div>
  <h3>Frieght Forwarding</h3>
  <p>Lorem ipsum dolor sit amet,<br>consectetur adipiscing elit, sed<br>do eiusmod tempor incididunt ut</p>
</div>

<div class="btn" style="left:488px;top:1513px;width:225px;height:37px">Sign up now</div>

<section class="ship-band" role="img" aria-label="Photo of stacked shipping containers and port cranes under a navy overlay">
  <h2>You can shop online and<br>We will take care of the shipment</h2>
  <p>Ships from United States of America to Jamaica</p>
  <div class="btn" style="left:488px;top:190px;width:225px;height:37px">Sign up now</div>
</section>

<h2 class="section-title" style="top:1993px">How It Works?</h2>

<div class="step" style="left:110px;top:2060px">
  <svg width="80" height="70" viewBox="0 0 80 70" fill="none" stroke="#0b2c5a" stroke-width="2.5"><rect x="4" y="4" width="72" height="50" rx="3"/><rect x="12" y="11" width="56" height="35"/><rect x="28" y="20" width="24" height="18" rx="2"/><path d="M33 26h14M33 32h10M40 54v8M22 66h36"/></svg>
  <h4>Sign Up</h4>
</div>
<div class="step" style="left:393px;top:2060px">
  <svg width="80" height="70" viewBox="0 0 80 70" fill="none" stroke="#0b2c5a" stroke-width="2.5"><rect x="4" y="14" width="62" height="38" rx="6"/><text x="14" y="43" font-family="Poppins,sans-serif" font-size="20" fill="#0b2c5a" stroke="none">BUY</text><path d="M52 40l16 18-6 1 4 8-4 2-4-8-5 4z" fill="#fff"/><path d="M35 2v6M20 6l3 5M50 6l-3 5"/></svg>
  <h4>Buy Online</h4>
</div>
<div class="step" style="left:670px;top:2060px">
  <svg width="80" height="70" viewBox="0 0 80 70" fill="none" stroke="#0b2c5a" stroke-width="2.5"><path d="M10 20c0-6 4-10 8-10l6 10-5 6c3 8 10 15 18 18l6-5 10 6c0 5-4 9-10 9C24 54 10 38 10 20z"/><rect x="36" y="2" width="40" height="22" rx="4"/><text x="41" y="19" font-family="Poppins,sans-serif" font-size="13" fill="#0b2c5a" stroke="none">24/7</text></svg>
  <h4>Schedule Pick-Up</h4>
</div>
<div class="step" style="left:915px;top:2060px">
  <svg width="80" height="74" viewBox="0 0 80 74" fill="none" stroke="#0b2c5a" stroke-width="2.5"><rect x="24" y="4" width="34" height="30"/><path d="M35 4v10l6-4 6 4V4M4 44h10v26H4zM14 48h18l10 6H28M14 66h30l30-22-8-4-20 12"/></svg>
  <h4 style="margin-top:32px">Deliver</h4>
</div>

<svg class="arrow" style="left:305px;top:2117px" width="46" height="16" viewBox="0 0 46 16" fill="none" stroke="#f0a80f" stroke-width="2"><path d="M0 8h44M36 1l8 7-8 7"/></svg>
<svg class="arrow" style="left:616px;top:2117px" width="46" height="16" viewBox="0 0 46 16" fill="none" stroke="#f0a80f" stroke-width="2"><path d="M0 8h44M36 1l8 7-8 7"/></svg>
<svg class="arrow" style="left:860px;top:2117px" width="46" height="16" viewBox="0 0 46 16" fill="none" stroke="#f0a80f" stroke-width="2"><path d="M0 8h44M36 1l8 7-8 7"/></svg>

<div class="btn" style="left:491px;top:2227px;width:225px;height:37px">Sign up now</div>

<section class="shops"></section>
<h2 class="section-title" style="top:2406px">Recommneded Online Shops</h2>
<div class="shop" style="left:111px">Pellane</div>
<div class="shop" style="left:268px">Corvane</div>
<div class="shop" style="left:444px">Halvern</div>
<div class="shop" style="left:612px">Ostrade</div>
<div class="shop" style="left:773px">Kinmoor</div>
<div class="shop" style="left:939px">Tarrow</div>

<footer class="site-footer">
  <div class="brand" style="left:158px;top:97px;color:var(--white)"><span class="dot"></span>Brightwell Cargo</div>
  <div class="rule" style="top:172px"></div>
  <h5 style="left:157px;top:192px">Address</h5>
  <p class="small" style="left:157px;top:215px">Shop 6 Brindley Commercial Complex,<br>207-209 Pellman Road Kingston 8,<br>Jamaica West Indies</p>
  <div class="rule" style="top:282px"></div>
  <h5 style="left:157px;top:302px">Telephone</h5>
  <p class="small" style="left:157px;top:326px">(876)555-0192</p>

  <h5 style="left:522px;top:72px">Quick Links</h5>
  <nav class="links">
    <a style="top:95px">About</a>
    <a style="top:125px">Services</a>
    <a style="top:155px">FAQs</a>
    <a style="top:185px">Contact</a>
    <a style="top:215px">Jobs</a>
  </nav>

  <h5 style="left:742px;top:71px">Join Our Newsletter</h5>
  <p class="small" style="left:741px;top:95px">Lorem ipsum dolor sit amet, consectetur</p>
</footer>
<div class="newsletter"><span>Your Email</span><div class="submit">SUBMIT</div></div>

</body>
</html>
```